flyer/brochure design to deliver to homes (letter box delivery)

Hi I would like something designed to represent my business Hair & Make up, I have a home based salon but offer mobile services for weddings. I really like beachy colours elegant and not to busy. but open to all different designs.

I will be getting these printed up through Lumaro print the product specs are:

Document Trim Size
Horizontal
216 x 139 mm
2556 x 1642 pixels
Vertical
139 x 216 mm
1642 x 2556 pixels

Full Bleed Size
Horizontal
219 x 142 mm
2592 x 1677 pixels
Vertical
142 x 219 mm
1677 x 2592 pixels
Finished artwork should use the full bleed dimensions for best results.

I will also upload a recent business card that i have but dont have to stick to similar design

Industry/Entity Type

Salon

Requirements
Must have
• my logo (you can change the colour of my logo if you like)

would like it to have somewhere:
"look good feel great without paying silly prices"

must also have:

private home salon based in Coral Cove, mobile service provided for weddings only

Im thinking I would like the price list on the back but open to what ever you submit

price list:
Ladies Cut $20
Ladies Blowdry $20 from
Mens cut $15
Full head of Foils, Toner, Cut & Blowdry $110
Half Head of Foils, Toner, Cut & Blowdry $80
Tint cut & colour $60-80
Tint with scattered foils Cut & Blowdry $70-$110

Wedding Package Hair & Make up $135pp mobile servive provided
check out our webpage for our complete pricelist

prices subject to change without notice

business details:

p: 0491 572 308
E: wbs@quorlin.com.au
W: www.willowbloomstudio.com.au

I would like it to have maybe on the front as an initial eye catcher:

Full head of foils, Toner, Cut & Blowdry $110 every day

```html
<!DOCTYPE html>
<html lang="en">
<head>
<meta charset="utf-8">
<title>Willow Bloom Studio – Flyer</title>
<link rel="stylesheet" href="https://fonts.googleapis.com/css2?family=Cinzel:wght@400;600;700&family=Marcellus&family=Pinyon+Script&display=swap">
<style>
  :root{
    --copper:#b77a58;
    --copper-dark:#9a6044;
    --copper-light:#d9a788;
    --cream:#f3e6dc;
    --white:#ffffff;
    --frame:#9a9a9a;
  }
  *{box-sizing:border-box;margin:0;padding:0}
  html,body{width:1200px;height:912px;overflow:hidden;background:var(--white)}
  body{position:relative;font-family:"Cinzel",serif}

  /* ---------- front ---------- */
  .front{position:absolute;left:7px;top:7px;width:594px;height:902px;border:1px solid var(--frame);overflow:hidden;background:var(--white)}
  .front__photo{position:absolute;left:0;top:0;width:100%;height:568px;
    background:
      radial-gradient(ellipse 45% 60% at 62% 48%, #c9b29b 0%, rgba(201,178,155,0) 70%),
      radial-gradient(ellipse 30% 40% at 20% 18%, #dccbbb 0%, rgba(220,203,187,0) 80%),
      linear-gradient(160deg,#cdbcaa 0%,#a78b74 45%,#6f5646 100%);}
  .badge{position:absolute;left:26px;top:32px;width:156px;height:156px;border-radius:50%;
    background:radial-gradient(circle at 40% 35%,var(--copper-light),var(--copper) 70%,var(--copper-dark));
    display:flex;align-items:center;justify-content:center;}
  .badge__text{transform:rotate(-30deg);text-align:center;color:var(--white);font-family:"Cinzel",serif;font-weight:700;font-size:16px;line-height:1.05;text-transform:uppercase}
  .badge__price{font-size:22px;display:block}

  .headline{position:absolute;left:32px;top:336px;color:var(--white);font-family:"Marcellus",serif;font-weight:400;font-size:72px;line-height:74px;text-transform:uppercase;letter-spacing:1px}
  .headline strong{font-weight:700;font-family:"Cinzel",serif}

  .tagline-band{position:absolute;left:0;top:572px;width:100%;height:48px;background:rgba(243,230,220,.88);display:flex;align-items:center;justify-content:center}
  .tagline{color:var(--copper);font-family:"Cinzel",serif;font-weight:600;font-size:26px;letter-spacing:.5px}

  .contact-band{position:absolute;left:0;top:624px;width:100%;height:162px;background:linear-gradient(90deg,var(--copper) 0%,var(--copper-light) 55%,var(--copper) 100%);color:var(--white);text-align:center}
  .contact-band__salon{margin-top:14px;font-size:22px;letter-spacing:.5px}
  .contact-band__mobile{margin-top:4px;font-size:16px;letter-spacing:.5px}
  .contact-band__phone{margin-top:12px;font-family:"Marcellus",serif;font-weight:400;font-size:48px;letter-spacing:3px;line-height:1}
  .contact-band__web{margin-top:8px;font-size:14px;letter-spacing:.5px}

  .brand{position:absolute;left:0;top:800px;width:100%;text-align:center;color:var(--copper-dark);font-family:"Cinzel",serif;font-weight:600;font-size:30px;line-height:34px;letter-spacing:1px}

  /* ---------- back ---------- */
  .back{position:absolute;left:615px;top:7px;width:582px;height:902px;border:1px solid var(--frame);
    background:linear-gradient(120deg,var(--copper-dark) 0%,var(--copper) 30%,var(--copper-light) 60%,var(--copper) 100%);overflow:hidden}
  .back__title{position:absolute;top:22px;width:100%;text-align:center;color:var(--white);font-family:"Cinzel",serif;font-size:62px;font-weight:400;letter-spacing:2px}
  .price-panel{position:absolute;left:34px;top:109px;width:518px;height:772px;border-radius:22px;background:rgba(255,235,222,.22);color:var(--white);text-align:center;padding-top:20px}
  .price-item{margin-bottom:26px}
  .price-item__name{font-size:17px;letter-spacing:1px;font-variant:small-caps;line-height:20px}
  .price-item__price{font-size:17px;line-height:22px}
  .wedding__title{font-family:"Pinyon Script",cursive;font-size:34px;line-height:40px;margin-top:6px;margin-bottom:16px}
  .note{font-size:14px;letter-spacing:.5px;line-height:22px}
  .note--small{font-size:12px;margin-top:4px}
  .note--spaced{margin-top:30px}
</style>
</head>
<body>

<section class="front">
  <div class="front__photo" role="img" aria-label="Photo of a woman with long straight glossy honey-blonde hair and a full fringe, in profile"></div>

  <div class="badge">
    <p class="badge__text">Full head<br>of foils,<br>Toner, Cut<br>&amp; Blowdry<span class="badge__price">$110</span>every day</p>
  </div>

  <h1 class="headline">Look<br><strong>Good</strong> and<br>Feel <strong>Great</strong></h1>

  <div class="tagline-band"><p class="tagline">WITHOUT PAYING SILLY PRICES</p></div>

  <div class="contact-band">
    <p class="contact-band__salon">PRIVATE HOME SALON BASED IN CORAL COVE</p>
    <p class="contact-band__mobile">MOBILE SERVICE IS PROVIDED FOR WEDDINGS ONLY</p>
    <p class="contact-band__phone">0491 572 308</p>
    <p class="contact-band__web">WWW.WILLOWBLOOMSTUDIO.COM.AU</p>
  </div>

  <p class="brand">WILLOW BLOOM<br>STUDIO</p>
</section>

<section class="back">
  <h2 class="back__title">PRICE LIST</h2>
  <div class="price-panel">
    <div class="price-item"><p class="price-item__name">Ladies Cut</p><p class="price-item__price">$20</p></div>
    <div class="price-item"><p class="price-item__name">Ladies Blowdry</p><p class="price-item__price">From $20</p></div>
    <div class="price-item"><p class="price-item__name">Mens cut</p><p class="price-item__price">$15</p></div>
    <div class="price-item"><p class="price-item__name">Full head of Foils, Toner, Cut &amp; Blowdry</p><p class="price-item__price">$110</p></div>
    <div class="price-item"><p class="price-item__name">Half Head of Foils, Toner, Cut &amp; Blowdry</p><p class="price-item__price">$80</p></div>
    <div class="price-item"><p class="price-item__name">Tint cut &amp; colour</p><p class="price-item__price">$60-80</p></div>
    <div class="price-item"><p class="price-item__name">Tint with scattered foils Cut &amp; Blowdry</p><p class="price-item__price">$70-$110</p></div>

    <div class="wedding">
      <p class="wedding__title">Wedding Package</p>
      <p class="price-item__name">Hair &amp; Make up</p>
      <p class="price-item__price">$135pp</p>
      <p class="note note--small">MOBILE SERVICE PROVIDED</p>
    </div>

    <p class="note note--spaced">CHECK OUT OUR WEBPAGE<br>FOR OUR COMPLETE PRICELIST</p>
    <p class="note note--small note--spaced">PRICES SUBJECT TO CHANGE WITHOUT NOTICE</p>
  </div>
</section>

</body>
</html>
```